A specialised Sport management needs a corporate brochure design

We are a specialized company in the management and consultancy of sports events. and need to have a company brochure
We provide the following services;
Event management
Venues management
Production
Ticketing
Consulting
Hospitality
Activity management
Event timing
Branding of event
Event supplies
We need a corporate profile design for our company to showcase the major events that we have covered , with images, information, statistics, surveys, products and services used. We want to highlight our professionalism and execution of the events, experience of the participants, spectators . How we have grown in the past few years and reached the international standards.
Objectives of the work:
To get sponsors and partners for future business and to present Keel-Marrow
as not just a sports management company but also a professional sports
events management company.
You can check our website
www.keel-marrow.example
Target Market(s)
Sponsors and corporate partners
Industry/Entity Type
Events
Font styles to use
Requirements
Must have
- Must Have:
- - Very professional look
- -Some event images,Event information, statistics, surveys, products and services used. We want to highlight our professionalism and execution of the events (Attached)
Nice to have
- Similar momentom of the below design
- http://www.dunlathgames.example/wp-content/themes/dunlath_games/pdf/CP-2014-15-V10-Web.pdf

```html
<!DOCTYPE html>
<html lang="en">
<head>
<meta charset="utf-8">
<title>Keel-Marrow – Corporate Brochure</title>
<link rel="stylesheet" href="https://fonts.googleapis.com/css2?family=Open+Sans:ital,wght@0,400;0,600;0,700;1,400&display=swap">
<style>
:root{
  --board:#000;
  --paper:#fff;
  --ink:#4a4a4a;
  --ink-soft:#7a7a7a;
  --night:#26252a;
  --orange:#f39a1e;
  --green:#3c9f48;
  --line:#c9c9c9;
  --grey-figure:#8a8a8a;
}
*{box-sizing:border-box;margin:0;padding:0}
html,body{width:848px;height:1200px;overflow:hidden;background:var(--board)}
body{position:relative;font-family:"Open Sans",Arial,sans-serif;color:var(--ink)}
.spread{position:absolute;left:36px;width:764px;height:268px;background:var(--paper);overflow:hidden}
.spread--cover{top:50px}
.spread--about{top:362px}
.spread--stats{top:702px}
.spread svg.art{position:absolute;inset:0;width:764px;height:268px}
.abs{position:absolute}

/* brand mark */
.mark{position:absolute;display:flex;align-items:center;gap:4px;font-weight:700;white-space:nowrap}
.mark__dot{border-radius:50%;background:var(--orange);flex:none}
.mark--light{color:#fff}
.mark--dark{color:var(--night)}

/* cover */
.contact{left:46px;top:182px;font-size:6px;line-height:8.4px;color:#333}
.contact b{font-weight:700}
.contact .site{font-weight:700}
.contact .handle{margin-top:8px;display:flex;align-items:center;gap:4px}
.recycle-note{left:214px;top:222px;width:86px;font-size:3.6px;line-height:4.4px;color:#777;text-align:right}
.partner-badge{left:304px;top:222px;width:22px;height:9px;background:#d6d6d6;border-radius:2px}
.cover-title{left:478px;top:196px;font-size:17.5px;line-height:21px;color:var(--orange);font-weight:400;letter-spacing:.2px}

/* about */
.about-copy{left:34px;top:10px;width:230px;font-size:5.4px;line-height:7px;color:var(--ink)}
.about-copy .lead{font-size:7.6px;color:#222}
.about-copy h3{color:var(--green);font-size:8px;font-weight:600;margin-top:5px}
.testimonial{left:34px;top:162px;width:130px;font-size:6.2px;line-height:8px;font-style:italic;color:var(--ink-soft)}
.testimonial .who{font-style:normal;color:#333;margin-top:6px;font-size:6.4px}
.testimonial .role{font-style:normal;color:var(--ink-soft);font-size:5.6px}
.quote-band{left:452px;top:36px;width:260px;font-size:6px;line-height:7.4px;font-style:italic;color:#fff}
.quote-band .who{font-style:normal;font-size:6.2px;margin-top:3px}
.segment{font-size:5.2px;line-height:6.4px;color:#333}
.segment h3{color:var(--green);font-size:8px;font-weight:600;line-height:9px}
.segment h2{color:#555;font-size:9px;font-weight:400;margin-bottom:3px}
.seg-public{left:414px;top:114px;width:108px}
.seg-engaged{left:414px;top:200px;width:86px}
.seg-athletes{left:646px;top:202px;width:96px}

/* stats */
.stats-box{left:22px;top:84px;width:166px;height:140px;border:1px solid #6a6a6a}
.stat{position:absolute;color:#e6e6e6;font-size:5.6px;line-height:7px}
.stat .num{font-size:10px;line-height:12px;color:#fff}
.stat .rule{width:64px;height:2px;background:var(--orange);margin-top:3px}
.stats-title{left:32px;top:88px;font-size:8px;color:var(--orange)}
.growth-title{left:208px;top:94px;font-size:8px;color:var(--orange)}
.growth-row{position:absolute;left:208px;display:flex;align-items:center;gap:4px;font-size:5.4px;color:#ddd}
.year-tag{background:var(--green);color:#fff;font-weight:700;padding:1px 3px;font-size:5.4px}
.marketing{left:416px;top:42px;width:118px;font-size:5.4px;line-height:6.8px;color:#444}
.marketing h2{font-size:9.5px;font-weight:400;color:#555;margin-bottom:8px}
.marketing h3{font-size:7.6px;font-weight:600;color:var(--green);margin-top:6px}
</style>
</head>
<body>

<!-- Spread 1: back and front cover -->
<section class="spread spread--cover">
  <svg class="art" viewBox="0 0 764 268" aria-hidden="false">
    <defs>
      <linearGradient id="runnersTone" x1="0" y1="0" x2="1" y2="1">
        <stop offset="0" stop-color="#7e9cc0"/><stop offset="1" stop-color="#4b8a3d"/>
      </linearGradient>
      <linearGradient id="raceTone" x1="0" y1="0" x2="0" y2="1">
        <stop offset="0" stop-color="#c9b28c"/><stop offset="1" stop-color="#5e5a57"/>
      </linearGradient>
      <linearGradient id="climbTone" x1="0" y1="0" x2="1" y2="1">
        <stop offset="0" stop-color="#8fb6dc"/><stop offset="1" stop-color="#c98b6a"/>
      </linearGradient>
    </defs>
    <rect x="382" y="0" width="382" height="268" fill="var(--night)"/>
    <polygon points="508,0 612,0 512,185 408,185" fill="url(#runnersTone)" role="img" aria-label="Photo: trail runner in a green shirt on a sunny course"/>
    <polygon points="626,0 706,0 606,185 526,185" fill="url(#raceTone)" role="img" aria-label="Photo: crowd of marathon runners at a city race start"/>
    <polygon points="720,0 764,0 764,54 690,185 622,185" fill="url(#climbTone)" role="img" aria-label="Photo: obstacle racer climbing a rope against the sky"/>
    <rect x="762" y="0" width="2" height="268" fill="#cfcfcf"/>
  </svg>

  <div class="mark mark--dark" style="left:58px;top:120px;font-size:10px"><span class="mark__dot" style="width:14px;height:14px"></span>Keel-Marrow</div>

  <div class="abs contact">
    <div><b>Mob:</b> 965 4100 2781</div>
    <div><b>Tel:</b> 965 4100 2790</div>
    <div><b>Email:</b> events@keel-marrow.example</div>
    <div class="site">www.keel-marrow.example</div>
    <div class="handle">
      <svg width="8" height="7" viewBox="0 0 8 7" aria-hidden="true"><path d="M1 3.5h6M4.5 1l2.5 2.5L4.5 6" stroke="#4aa3df" stroke-width="1.2" fill="none"/></svg>
      <span>@kmsportevents</span>
    </div>
  </div>

  <p class="abs recycle-note">Printed on fully recycled stock using certified low-impact inks and water-based coatings. Please pass this brochure on or recycle it when you are done.</p>
  <div class="abs partner-badge"></div>

  <div class="mark mark--light" style="left:398px;top:204px;font-size:9px"><span class="mark__dot" style="width:16px;height:16px;background:#fff"></span>Keel-Marrow</div>
  <h1 class="abs cover-title">SPORTS &amp; EVENT<br>MANAGEMENT SPECIALISTS</h1>
</section>

<!-- Spread 2: about and target segments -->
<section class="spread spread--about">
  <svg class="art" viewBox="0 0 764 268">
    <defs>
      <linearGradient id="swimTone" x1="0" y1="0" x2="0" y2="1">
        <stop offset="0" stop-color="#9eb7cf"/><stop offset=".45" stop-color="#c7a84a"/><stop offset="1" stop-color="#3f4a52"/>
      </linearGradient>
      <linearGradient id="desertTone" x1="0" y1="0" x2="1" y2="1">
        <stop offset="0" stop-color="#d9d9db"/><stop offset="1" stop-color="#b9aa98"/>
      </linearGradient>
      <linearGradient id="hikerTone" x1="0" y1="0" x2="0" y2="1">
        <stop offset="0" stop-color="#5f8fc4"/><stop offset="1" stop-color="#8b6b52"/>
      </linearGradient>
    </defs>
    <polygon points="342,0 422,0 292,268 142,268" fill="url(#swimTone)" role="img" aria-label="Photo: triathletes in yellow caps running into the sea at the swim start"/>
    <polygon points="432,70 764,70 764,268 330,268" fill="url(#desertTone)" opacity=".75" role="img" aria-label="Photo: rocky desert landscape under a hazy sky"/>
    <polygon points="574,70 650,70 556,268 470,268" fill="url(#hikerTone)" role="img" aria-label="Photo: athlete in red scaling a rock face"/>
    <polygon points="764,150 764,268 650,268" fill="#fff" opacity=".55"/>
    <polygon points="386,30 750,30 734,70 386,70" fill="var(--orange)"/>
  </svg>

  <div class="abs about-copy">
    <p class="lead">Keel-Marrow <span style="font-size:5.4px;color:var(--ink)">is the leading company in Kuwait, which specializes in the management and consultancy of sports events. Established in 2007, Keel-Marrow has grown in stature and strength over the years, to become the renowned establishment it is today in this highly specialized field.</span></p>
    <h3>Our Goal</h3>
    <p>Raise awareness of sport practice and creating exciting sport events with international standards. Allowing every individual to participate in different types of sport events for all levels. Each year we get closer to our goal to promote active lifestyle and sports activities in the country. We believe our partners play a major role in the contribution towards our goal for the society.</p>
  </div>

  <div class="abs testimonial">
    <p>"Haven't tried any Event managers before Keel-Marrow, don't want to try any others"</p>
    <p class="who">Faisal Qadri</p>
    <p class="role">Founder Loopline</p>
  </div>

  <div class="mark mark--light" style="left:392px;top:42px;font-size:7px"><span class="mark__dot" style="width:18px;height:18px;background:#fff"></span></div>
  <div class="abs quote-band">
    <p>"Awesome people, awesome events, thank you for renewing the hope of sports in Kuwait"</p>
    <p class="who">Tarek Nasrallah</p>
  </div>

  <div class="abs segment seg-public">
    <h2>Target Segment</h2>
    <h3>Mainstream Public</h3>
    <p>This is a huge audience reached predominantly through the mainstream print and digital coverage. They are captivated and inspired by the incredible feats of sport events and determination displayed by the athletes. Estimated number of mainstream audience is 50,000</p>
  </div>
  <div class="abs segment seg-engaged">
    <h3>Engaged</h3>
    <p>This segment encompasses all those who are engaged directly with us, but not necessarily a current athlete.</p>
  </div>
  <div class="abs segment seg-athletes">
    <h3>Athletes</h3>
    <p>Majority of athletes are ranging between 20 - 45 years old, %70 Male and %30 Female , with high disposable incomes. They are fit, motivated and looking to challenge themselves.</p>
  </div>
</section>

<!-- Spread 3: statistics and marketing -->
<section class="spread spread--stats">
  <svg class="art" viewBox="0 0 764 268">
    <defs>
      <linearGradient id="fieldTone" x1="0" y1="0" x2="1" y2="0">
        <stop offset="0" stop-color="#c48a25"/><stop offset=".5" stop-color="#e0a83a"/><stop offset="1" stop-color="#9a6a24"/>
      </linearGradient>
      <linearGradient id="carTone" x1="0" y1="0" x2="1" y2="1">
        <stop offset="0" stop-color="#ececec"/><stop offset=".55" stop-color="#8f98a8"/><stop offset="1" stop-color="#2c3550"/>
      </linearGradient>
    </defs>
    <rect x="0" y="0" width="382" height="268" fill="var(--night)"/>
    <polygon points="4,42 350,42 334,78 4,78" fill="url(#fieldTone)" role="img" aria-label="Photo: mass start of runners on a sunlit field"/>
    <polygon points="636,0 764,0 764,268 470,268" fill="url(#carTone)" role="img" aria-label="Photo: single-seater race car speeding past, motion blurred"/>
    <rect x="762" y="0" width="2" height="268" fill="#cfcfcf"/>
  </svg>

  <div class="mark mark--light" style="left:350px;top:14px"><span class="mark__dot" style="width:24px;height:24px;background:#fff"></span></div>

  <div class="abs stats-box"></div>
  <p class="abs stats-title">Number of participates in 2014</p>
  <div class="stat" style="left:32px;top:100px"><div class="num">10,000</div></div>
  <div class="stat" style="left:32px;top:122px">Number of sports<br>13<br>Visitors<div class="num">+30,000</div><div class="rule"></div></div>
  <div class="stat" style="left:32px;top:176px">Said they would rate our<br>events as "Excellent" in our<br>survey (average)<div class="num">86%</div><div class="rule"></div></div>
  <div class="stat" style="left:112px;top:122px">Said they would<br>participate<br>again (average)<div class="num">84%</div><div class="rule"></div></div>
  <div class="stat" style="left:112px;top:176px">Said they recognized<br>our sponsors (average)<div class="num">80%</div><div class="rule"></div></div>

  <p class="abs growth-title">Growth Over the Years</p>

  <div class="growth-row" style="top:110px"><span class="year-tag">2011</span><span style="width:52px">Participants 1,300</span>
    <svg width="100" height="12" viewBox="0 0 100 12"><g fill="var(--grey-figure)"><use href="#fig" x="0"/></g></svg></div>
  <div class="growth-row" style="top:134px"><span class="year-tag">2012</span><span style="width:52px">Participants 2,700</span>
    <svg width="100" height="12" viewBox="0 0 100 12"></svg></div>
  <div class="growth-row" style="top:158px"><span class="year-tag">2013</span><span style="width:52px">Participants 5,800+</span>
    <svg width="100" height="12" viewBox="0 0 100 12"></svg></div>
  <div class="growth-row" style="top:182px"><span class="year-tag">2014</span><span style="width:52px">Participants 10,000+</span>
    <svg width="100" height="12" viewBox="0 0 100 12"></svg></div>

  <!-- participant figure rows -->
  <svg class="abs" style="left:288px;top:110px" width="100" height="96" viewBox="0 0 100 96" aria-hidden="true">
    <defs>
      <g id="person"><circle cx="2.5" cy="1.6" r="1.5"/><rect x="0.6" y="3.4" width="3.8" height="8" rx="1"/></g>
    </defs>
    <g transform="translate(0,0)">
      <g fill="var(--orange)"><use href="#person" x="0"/></g>
      <g fill="var(--grey-figure)">
        <use href="#person" x="6"/><use href="#person" x="12"/><use href="#person" x="18"/><use href="#person" x="24"/><use href="#person" x="30"/><use href="#person" x="36"/><use href="#person" x="42"/><use href="#person" x="48"/><use href="#person" x="54"/><use href="#person" x="60"/><use href="#person" x="66"/><use href="#person" x="72"/><use href="#person" x="78"/>
      </g>
    </g>
    <g transform="translate(0,24)">
      <g fill="var(--orange)"><use href="#person" x="0"/><use href="#person" x="6"/><use href="#person" x="12"/></g>
      <g fill="var(--grey-figure)">
        <use href="#person" x="18"/><use href="#person" x="24"/><use href="#person" x="30"/><use href="#person" x="36"/><use href="#person" x="42"/><use href="#person" x="48"/><use href="#person" x="54"/><use href="#person" x="60"/><use href="#person" x="66"/><use href="#person" x="72"/><use href="#person" x="78"/>
      </g>
    </g>
    <g transform="translate(0,48)">
      <g fill="var(--orange)"><use href="#person" x="0"/><use href="#person" x="6"/><use href="#person" x="12"/><use href="#person" x="18"/><use href="#person" x="24"/><use href="#person" x="30"/><use href="#person" x="36"/></g>
      <g fill="var(--grey-figure)">
        <use href="#person" x="42"/><use href="#person" x="48"/><use href="#person" x="54"/><use href="#person" x="60"/><use href="#person" x="66"/><use href="#person" x="72"/><use href="#person" x="78"/>
      </g>
    </g>
    <g transform="translate(0,72)" fill="var(--orange)">
      <use href="#person" x="0"/><use href="#person" x="6"/><use href="#person" x="12"/><use href="#person" x="18"/><use href="#person" x="24"/><use href="#person" x="30"/><use href="#person" x="36"/><use href="#person" x="42"/><use href="#person" x="48"/><use href="#person" x="54"/><use href="#person" x="60"/><use href="#person" x="66"/><use href="#person" x="72"/><use href="#person" x="78"/>
    </g>
  </svg>

  <div class="abs marketing">
    <h2>Marketing</h2>
    <h3>Social Media</h3>
    <p>With over 30,000 visitors and 10,000 participants, Keel-Marrow events are the perfect opportunity to take advantage of Social Media as it's the leading marketing tool in the industry. Take advantage of audience by engaging them in competitions and marketing campaigns.</p>
    <h3>Branding</h3>
    <p>In addition to CSR benefits – companies will be mentioned in all communications and branding outlets will be prominently displayed on location and media distributions.</p>
  </div>

  <div class="mark mark--dark" style="left:712px;top:238px"><span class="mark__dot" style="width:22px;height:22px"></span></div>
</section>

</body>
</html>
```